3-4 Page Research Report Template

We want a template in MS Word that we can use to write up research reports. We want a similar feal as our newsletter and website - but we also want it to look more modern, yet stay in the financial service / investment research world.

Examples: http://media.valtrona.com/Documents/Asset_Allocation_Focus_March2013.pdf

http://www.brellick.com/Home/Documents/Default.aspx?fileId=58082

Our website: www.dunmoreplanners.com
Our Newsletter: http://www.dunmoreplanners.com/HaldenBrief/2012/2012-11-12.pdf

We want 3 template pages - a cover or 1st page, a middle page and and last or end page.

Project Deadline Extended
Reason: I would like more than two designers to compare ideas. I was hoping for 5. This is designers not designs.

We are not looking for a new version of our Newsletter "The Halden Brief" - We want a template to publish other research articles. We shared The Halden Brief file to give you a better idea on what we currently like / use - though dated as it was designed in 2004. 

That doesn't mean we wont pick a template using The Halden Brief as example content. I just wanted to be clear. 

Target Market(s)

Sophisticated investors with over $1M in the market and investment professionals (financial advisors)

Industry/Entity Type

Investment

Requirements
Must have
• Space for disclosures at the end.
Ability to drop in tables and charts/graphs
Should not have
• Do not use the DNMP website masthead directly. Please be creative in helping is get a more modern and fresh design. I provided it as reference on what we already like (or did in 2004 when it was designed).

```html
<!DOCTYPE html>
<html lang="en">
<head>
<meta charset="utf-8">
<title>The Halden Brief – Research Report Template</title>
<link rel="stylesheet" href="https://fonts.googleapis.com/css2?family=Source+Sans+3:wght@400;600;700&display=swap">
<style>
:root{
  --desk:#d5d9df;
  --paper:#ffffff;
  --ink:#4a4f57;
  --blue:#0a72c0;
  --blue-deep:#0b5e9e;
  --cyan:#1ab4e8;
  --teal:#2196c9;
  --red:#d9432f;
  --rule:#9aa3ad;
  --grid:#7e8a96;
  --pale:#dfe9f6;
  --logo-grey:#dfe2e6;
}
*{box-sizing:border-box;margin:0;padding:0}
html,body{width:1200px;height:750px;overflow:hidden}
body{background:var(--desk);font-family:"Source Sans 3",sans-serif;color:var(--ink);position:relative}
.stage{position:absolute;top:0;left:0;width:1200px;height:785px;transform:scale(.955);transform-origin:top center}
.page{position:absolute;width:560px;background:var(--paper);box-shadow:0 1px 4px rgba(0,0,0,.25);overflow:hidden}
.page--prev{top:0;height:34px}
.page--main{top:46px;height:724px}
.col-a{left:30px}
.col-b{left:610px}
.abs{position:absolute}
.body-text{font-size:7.8px;line-height:11px;color:var(--ink)}
.body-text p{margin-bottom:10px}
.masthead{top:24px;left:0;width:100%;text-align:center;font-size:8px;letter-spacing:6.5px;font-weight:600}
.masthead .title{color:var(--red)}
.masthead .sub{color:var(--teal)}
.masthead-rule{top:42px;left:42px;width:476px;height:1px;background:var(--rule)}
.section-bar{height:22px;background:linear-gradient(90deg,var(--cyan),var(--blue-deep));color:#fff;font-size:7.5px;font-weight:700;display:flex;align-items:center;justify-content:center;border-radius:2px}
.cover-bar{top:51px;left:30px;width:495px}
.col{overflow:hidden}
.col--left{top:82px;left:30px;width:236px;height:192px}
.col--right{top:82px;left:291px;width:236px;height:192px}
.caption{top:282px;left:0;width:100%;text-align:center;font-size:7px;font-weight:700;color:var(--blue)}
.returns{top:300px;left:30px;width:495px;border-collapse:collapse;font-size:6px;text-align:center}
.returns th,.returns td{border:1px solid var(--grid);height:16.4px}
.returns .company th{background:var(--blue);color:#fff;font-weight:700;border-color:var(--blue)}
.returns .heads th{font-weight:600;background:#f3f5f7}
.notes{top:452px;left:30px;width:495px;height:193px;border:1px solid var(--grid);padding:14px 6px;font-size:7.1px;line-height:10.6px;font-weight:400}
.notes p{margin-bottom:11px}
.footer{bottom:28px;font-size:6px;color:var(--teal)}
.page--prev .footer{bottom:12px}
.footer--left{left:30px}
.footer--right{right:30px}
.top-band{top:32px;left:0;width:100%;height:5px;background:var(--blue-deep)}
.top-band-light{top:32px;left:460px;width:100px;height:5px;background:var(--cyan)}
.logo{top:21px;left:338px;width:117px;height:90px;background:var(--logo-grey);border-radius:6px;box-shadow:0 2px 4px rgba(0,0,0,.2);display:flex;flex-direction:column;align-items:center;justify-content:center;gap:6px}
.logo .dot{width:26px;height:26px;border-radius:50%;background:#aab2bc}
.logo .name{font-size:8.5px;font-weight:600;color:var(--blue-deep);text-align:center;line-height:10px}
.review-bar{top:62px;left:32px;width:234px}
.col--review{top:96px;left:32px;width:238px;height:398px}
.signature{top:508px;left:32px;width:238px;height:84px;border:1px solid var(--grid)}
.signature .label{height:14px;border-bottom:1px solid var(--grid);font-size:6.5px;font-weight:600;text-align:center;line-height:13px}
.signature .art{position:absolute;top:20px;left:10px;right:10px;height:52px;background:var(--pale)}
.signature .frame{position:absolute;top:24px;left:93px;width:52px;height:48px;background:#6f8aa8;border:3px solid #c9d3de}
.staff{top:140px;left:346px;width:175px;font-size:6.8px;line-height:12.5px}
.staff .name{color:var(--blue-deep);font-weight:700;text-transform:uppercase}
.staff .role{color:var(--teal)}
.staff .member{margin-bottom:14px}
.publisher{top:372px;left:346px;width:175px;font-size:5.4px;line-height:10px}
.publisher a{color:var(--blue);font-weight:700}
.offering{top:504px;left:346px;width:175px;font-size:5.4px;line-height:10px}
.sidebar-rule{top:594px;left:294px;width:230px;height:1px;background:var(--rule)}
.disclaimer{top:614px;left:32px;width:496px;font-size:5.5px;line-height:9px}
</style>
</head>
<body>
<div class="stage">

<section class="page page--prev col-a" aria-label="Previous page"></section>
<section class="page page--prev col-b" aria-label="Middle page">
  <div class="abs footer footer--left">November/December 20XX</div>
  <div class="abs footer footer--right">© Dunmore Fund Planners</div>
</section>

<section class="page page--main col-a">
  <div class="abs masthead"><span class="title">THE HALDEN BRIEF:</span> <span class="sub">CLOSED END FUND REPORT</span></div>
  <div class="abs masthead-rule"></div>
  <div class="abs section-bar cover-bar">Commodities Boom Sees Global Growth</div>

  <div class="abs col col--left body-text">
    <p>Lorem ipsum dolor sit amet, consectetuer adipiscing elit. Maecenas porttitor congue massa. Fusce posuere, magna sed pulvinar ultricies, purus lectus malesuada libero, sit amet commodo magna eros quis urna. Nunc viverra imperdiet enim. Fusce est. Vivamus a tellus.</p>
    <p>Pellentesque habitant morbi tristique senectus et netus et malesuada fames ac turpis egestas. Proin pharetra nonummy pede. Mauris et orci. Aenean nec lorem. In porttitor. Donec laoreet nonummy augue.</p>
    <p>Suspendisse dui purus, scelerisque at, vulputate vitae, pretium mattis, nunc. Mauris eget neque at sem venenatis eleifend. Ut nonummy. Fusce aliquet pede non pede. Suspendisse dapibus lorem pellentesque magna. Integer nulla.</p>
  </div>
  <div class="abs col col--right body-text">
    <p>pretium metus, in lacinia nulla nisl eget sapien. Donec ut est in lectus consequat consequat. Etiam eget dui. Aliquam erat volutpat. Sed at lorem in nunc porta tristique.</p>
    <p>Proin nec augue. Quisque aliquam tempor magna. Pellentesque habitant morbi tristique senectus et netus et malesuada fames ac turpis egestas. Nunc ac magna. Maecenas odio dolor, vulputate vel, auctor ac, accumsan id, felis. Pellentesque cursus sagittis felis. Lorem ipsum dolor sit amet, consectetuer adipiscing elit. Maecenas porttitor congue massa. Fusce posuere, magna sed pulvinar ultricies, purus lectus malesuada libero, sit amet commodo magna eros quis urna.</p>
  </div>

  <div class="abs caption">Total Returns</div>
  <table class="abs returns">
    <tr class="company"><th colspan="4">Sample Company Inc.</th></tr>
    <tr class="heads"><th>XXXXXX</th><th>XXXXXX</th><th>XXXXXXX</th><th>XXXXXXXX</th></tr>
    <tr><td>XX.XX.XX</td><td>XX.XX.XX</td><td>XX.XX.XX</td><td>XX.XX.XX</td></tr>
    <tr><td>XX.XX.XX</td><td>XX.XX.XX</td><td>XX.XX.XX</td><td>XX.XX.XX</td></tr>
    <tr><td>XX.XX.XX</td><td>XX.XX.XX</td><td>XX.XX.XX</td><td>XX.XX.XX</td></tr>
    <tr><td>XX.XX.XX</td><td>XX.XX.XX</td><td>XX.XX.XX</td><td>XX.XX.XX</td></tr>
    <tr><td>XX.XX.XX</td><td>XX.XX.XX</td><td>XX.XX.XX</td><td>XX.XX.XX</td></tr>
    <tr><td>XX.XX.XX</td><td>XX.XX.XX</td><td>XX.XX.XX</td><td>XX.XX.XX</td></tr>
    <tr><td>XX.XX.XX</td><td>XX.XX.XX</td><td>XX.XX.XX</td><td>XX.XX.XX</td></tr>
  </table>

  <div class="abs notes">
    <p>Proin nec augue. Quisque aliquam tempor magna. Pellentesque habitant morbi tristique senectus et netus et malesuada fames ac turpis egestas. Nunc ac magna. Maecenas odio dolor, vulputate vel, auctor ac, accumsan id, felis. Pellentesque cursus sagittis felis. Lorem ipsum dolor sit amet, consectetuer adipiscing elit. Maecenas porttitor congue massa. Fusce posuere, magna sed pulvinar ultricies, purus lectus malesuada libero, sit amet commodo magna eros quis urna.***</p>
    <p>Proin nec augue. Quisque aliquam tempor magna. Pellentesque habitant morbi tristique senectus et netus et malesuada fames ac turpis egestas. Nunc ac magna. Maecenas odio dolor, vulputate vel, auctor ac, accumsan id, felis. Pellentesque cursus sagittis felis. Lorem ipsum dolor sit amet, consectetuer adipiscing elit. Maecenas porttitor congue massa. Fusce posuere, magna sed pulvinar ultricies, purus lectus malesuada libero, sit amet commodo magna eros quis urna.</p>
    <p>Proin nec augue. Quisque aliquam tempor magna. Pellentesque habitant morbi tristique senectus et netus et malesuada fames ac turpis egestas. Nunc ac magna. Maecenas odio dolor, vulputate vel, auctor ac, accumsan id, felis. Pellentesque cursus sagittis felis. Lorem ipsum dolor sit amet, consectetuer adipiscing elit. Maecenas porttitor congue massa. Fusce posuere, magna sed pulvinar ultricies, purus lectus malesuada libero, sit amet commodo magna eros quis urna.</p>
  </div>

  <div class="abs footer footer--left">November/December 20XX</div>
  <div class="abs footer footer--right">© Dunmore Fund Planners</div>
</section>

<section class="page page--main col-b">
  <div class="abs top-band"></div>
  <div class="abs top-band-light"></div>
  <div class="abs logo"><span class="dot"></span><span class="name">Dunmore Fund<br>Planners</span></div>

  <div class="abs section-bar review-bar">Portfolio Manager's Review</div>
  <div class="abs col col--review body-text">
    <p>Lorem ipsum dolor sit amet, consectetuer adipiscing elit. Maecenas porttitor congue massa. Fusce posuere, magna sed pulvinar ultricies, purus lectus malesuada libero, sit amet commodo magna eros quis urna. Nunc viverra imperdiet enim. Fusce est. Vivamus a tellus.</p>
    <p>Pellentesque habitant morbi tristique senectus et netus et malesuada fames ac turpis egestas. Proin pharetra nonummy pede. Mauris et orci. Aenean nec lorem. In porttitor. Donec laoreet nonummy augue.</p>
    <p>Suspendisse dui purus, scelerisque at, vulputate vitae, pretium mattis, nunc. Mauris eget neque at sem venenatis eleifend. Ut nonummy. Fusce aliquet pede non pede. Suspendisse dapibus lorem pellentesque magna. Integer nulla.</p>
    <p>Pellentesque habitant morbi tristique senectus et netus et malesuada fames ac turpis egestas. Proin pharetra nonummy pede. Mauris et orci. Aenean nec lorem. In porttitor. Donec laoreet nonummy augue.</p>
    <p>Suspendisse dui purus, scelerisque at, vulputate vitae, pretium mattis, nunc. Mauris eget neque at sem venenatis eleifend. Ut nonummy. Fusce aliquet pede non pede. Suspendisse dapibus lorem pellentesque magna. Integer nulla.</p>
    <p>Pellentesque habitant morbi tristique senectus et netus et malesuada fames ac turpis egestas. Proin pharetra nonummy pede. Mauris et orci. Aenean nec lorem. In porttitor. Donec laoreet nonummy augue.</p>
    <p>Suspendisse dui purus, scelerisque at, vulputate vitae, pretium mattis, nunc. Mauris eget neque at sem venenatis eleifend.</p>
  </div>

  <div class="abs signature">
    <div class="label">Signature Panel</div>
    <div class="art" role="img" aria-label="Signature image placeholder"></div>
    <div class="frame" role="img" aria-label="Picture placeholder"></div>
  </div>

  <div class="abs staff">
    <div class="member"><div class="name">Warren Ashby</div><div class="role">Founder and Editor-in-Chief</div><div class="role">Portfolio Manager</div></div>
    <div class="member"><div class="name">Martin Ashby</div><div class="role">Contributing Author</div><div class="role">Portfolio Manager</div></div>
    <div class="member"><div class="name">Nora Jean Pellow</div><div class="role">Copy Editor</div></div>
    <div class="member"><div class="name">Irene Tam Colver</div><div class="role">Production Editor</div></div>
  </div>

  <div class="abs publisher">
    The Halden Brief Online is published by<br>
    Dunmore Fund Planners Global Investment Counsel<br>
    4410 Marlow Ridge Drive, Suite 210<br>
    Carver, Virginia 23999<br>
    (555) 014-2290<br>
    <a>www.dunmoreplanners.com</a>
  </div>

  <div class="abs offering">
    Currently offering managed portfolios with the following objectives:<br>
    International Equity<br>
    Globally Diversified Growth<br>
    Hybrid Income<br>
    Growth &amp; Income<br>
    Foundation/Balanced<br>
    Conservative Diversified
  </div>

  <div class="abs sidebar-rule"></div>

  <div class="abs disclaimer">
    Disclaimer: The views and opinions are as of the date of publication and are subject to change at any time based upon market or other conditions. None of the information contained herein should be construed as an offer to buy or sell securities or as recommendations. Performance results shown should not be considered indicative of future performance. Data is obtained from sources we believe to be reliable but cannot be guaranteed. Any reproduction of any part of The Halden Brief Closed-End Fund Report requires written permission from Dunmore Fund Planners. All rights reserved.
  </div>

  <div class="abs footer footer--left">November/December 20XX</div>
  <div class="abs footer footer--right">© Dunmore Fund Planners</div>
</section>

</div>
</body>
</html>
```